Crimson Thunder Dill Pickles needs your smart gourmet Design

Looking for a smart design for a dill pickle jar container. The text
Crimson Thunder Dill Pickles.
Simply Picklelicious.

A tasty reason to raid the refrigerator.

Target Market(s)

Foodies, farmers market types.

Font styles to use
Serif
Sans Serif

Colors

Designer to choose colors to be used in the design.

Requirements
Must have
• Attractive design to entice foodies to buy my Pickles. Not cluttered, easy to read.
Nice to have
• Pickles, garlic. Modern.
Should not have
• Clutter. No script text.

```html
<!DOCTYPE html>
<html lang="en">
<head>
<meta charset="utf-8">
<title>Crimson Thunder Dill Pickles – Jar Labels</title>
<link rel="stylesheet" href="https://fonts.googleapis.com/css2?family=Bebas+Neue&display=swap">
<style>
  :root {
    --backdrop: #eceee8;
    --label-paper: #ffffff;
    --ink-grey: #a3a3a3;
    --ink-teal: #037fa1;
  }
  html, body {
    margin: 0;
    padding: 0;
    width: 1200px;
    height: 821px;
    overflow: hidden;
    background: var(--backdrop);
  }
  .canvas {
    position: relative;
    width: 1200px;
    height: 821px;
    font-family: "Bebas Neue", "Oswald", sans-serif;
  }
  .jar-label {
    position: absolute;
    top: 128px;
    width: 400px;
    height: 565px;
    --ink: var(--ink-grey);
  }
  .jar-label--grey { left: 100px; }
  .jar-label--teal { left: 700px; --ink: var(--ink-teal); }

  .label-shape {
    position: absolute;
    inset: 0;
  }
  .label-shape path {
    fill: var(--label-paper);
    stroke: var(--ink);
    stroke-width: 10;
    stroke-linejoin: round;
  }
  .label-text {
    position: absolute;
    left: 0;
    width: 400px;
    margin: 0;
    text-align: center;
    color: var(--ink);
    font-weight: 400;
    white-space: nowrap;
  }
  .product-dill {
    top: 31px;
    font-size: 186px;
    line-height: 186px;
  }
  .product-pickles {
    top: 180px;
    font-size: 134px;
    line-height: 134px;
    letter-spacing: 0.01em;
  }
  .rule {
    position: absolute;
    left: 27px;
    width: 346px;
    height: 4px;
    background: var(--ink);
  }
  .rule--upper { top: 316px; }
  .rule--lower { top: 441px; }
  .brand-name {
    top: 331px;
    font-size: 40px;
    line-height: 44px;
    letter-spacing: 0.13em;
    padding-left: 0.13em;
    box-sizing: border-box;
  }
  .tagline-band {
    position: absolute;
    left: 5px;
    width: 390px;
    top: 384px;
    height: 67px;
    background: var(--ink);
  }
  .slogan {
    top: 388px;
    font-size: 32px;
    line-height: 32px;
  }
  .jar-label--teal .slogan {
    top: 401px;
    color: var(--label-paper);
  }
  .tagline {
    top: 456px;
    font-size: 36px;
    line-height: 44px;
    white-space: normal;
  }
  .jar-label--teal .tagline { top: 460px; }
</style>
</head>
<body>
<main class="canvas">

  <section class="jar-label jar-label--grey">
    <svg class="label-shape" width="400" height="565" viewBox="0 0 400 565" aria-hidden="true">
      <path d="M200 6 L370 68 Q394 78 394 102 L394 559 L6 559 L6 102 Q6 78 30 68 Z"/>
    </svg>
    <h1 class="label-text product-dill">DILL</h1>
    <h2 class="label-text product-pickles">PICKLES</h2>
    <div class="rule rule--upper"></div>
    <p class="label-text brand-name">CRIMSON THUNDER</p>
    <p class="label-text slogan">SIMPLY PICKLELICIOUS</p>
    <div class="rule rule--lower"></div>
    <p class="label-text tagline">A TASTY REASON TO RAID THE<br>REFRIGERATOR</p>
  </section>

  <section class="jar-label jar-label--teal">
    <svg class="label-shape" width="400" height="565" viewBox="0 0 400 565" aria-hidden="true">
      <path d="M200 6 L370 68 Q394 78 394 102 L394 559 L6 559 L6 102 Q6 78 30 68 Z"/>
    </svg>
    <h1 class="label-text product-dill">DILL</h1>
    <h2 class="label-text product-pickles">PICKLES</h2>
    <div class="rule rule--upper"></div>
    <p class="label-text brand-name">CRIMSON THUNDER</p>
    <div class="tagline-band"></div>
    <p class="label-text slogan">SIMPLY PICKLELICIOUS</p>
    <p class="label-text tagline">A TASTY REASON TO RAID THE<br>REFRIGERATOR</p>
  </section>

</main>
</body>
</html>
```